Real Estate Sales Window Card

We require a Window card for real estate sales and leasing.
K7 Residences is a wool store conversion located in the trendy, riverside suburb of Teneriffe, Brisbane. The clientele are generally professional couples working inner city jobs.
The card should reflect the style and colouring of the existing themes of the building, in particular the simple structural aspects with primary colours of black, white, grey, mocha and olive green.
For more details on the K7 residences please see http://k7residences-example.com.au/about/gallery/apartment-gallery (please note: disregard the red on the site as it is not part of the buildings tones)
The card should contain the following:
- Header
- Price
- Bed, Bath, Car
- Description
- Photo(s)
- Ad type (i.e. Sale or Lease)
The card will be used in A4 portrait and A3 landscape aspects.
Real Estate

```html
<!DOCTYPE html>
<html lang="en">
<head>
<meta charset="utf-8">
<title>K7 Residences – Window Card</title>
<link rel="stylesheet" href="https://fonts.googleapis.com/css2?family=Roboto+Condensed:wght@300;400;700&family=Open+Sans:wght@400;700&display=swap">
<style>
  :root {
    --black: #000000;
    --white: #ffffff;
    --band-grey: #4b4b4d;
    --text-grey: #bdbdbd;
    --tag-black: #111111;
    --price-red: #c8102e;
    --wood: #b4783c;
    --mocha: #6d5a48;
    --olive: #6f7d3a;
  }
  html, body {
    margin: 0;
    padding: 0;
    width: 848px;
    height: 1200px;
    overflow: hidden;
    background: var(--black);
  }
  .card {
    position: relative;
    width: 848px;
    height: 1200px;
    background: var(--black);
    overflow: hidden;
    font-family: "Roboto Condensed", "Arial Narrow", sans-serif;
    color: var(--white);
  }
  .photo { position: absolute; }
  .photo--bedroom {
    left: 0; top: 109px; width: 325px; height: 216px;
    background: linear-gradient(135deg, #d9d2c4 0%, #b4783c 40%, #8a5626 70%, #3b2a1c 100%);
  }
  .photo--living {
    left: 137px; top: 348px; width: 188px; height: 186px;
    background: linear-gradient(160deg, #cfd2d4 0%, #6c6c70 35%, #3c3a3a 65%, #8a5a34 100%);
  }
  .photo--kitchen {
    left: 623px; top: 0; width: 170px; height: 325px;
    background: linear-gradient(200deg, #c9c1b0 0%, #e6e3dc 30%, #8b8378 60%, #c79a62 100%);
  }
  .photo--exterior {
    left: 0; top: 747px; width: 848px; height: 345px;
    background:
      linear-gradient(90deg, rgba(80,110,40,0.85) 0%, rgba(110,125,58,0.6) 30%, rgba(0,0,0,0) 55%),
      linear-gradient(180deg, #9c9a90 0%, #d8c9a8 40%, #c99b5e 70%, #4e5a2a 100%);
  }
  .photo--exterior::after {
    content: "";
    position: absolute;
    right: 0; top: 0; width: 240px; height: 100%;
    background: linear-gradient(180deg, #a8d4e6 0%, #f4f6f2 35%, #8aa858 65%, #3c3c3c 100%);
  }

  .tag {
    position: absolute;
    left: 358px; top: 43px; width: 248px; height: 321px;
    background: var(--tag-black);
    text-align: center;
  }
  .tag__hole {
    position: absolute;
    left: 60px; top: -10px;
  }
  .tag__name {
    margin: 0;
    padding-top: 62px;
    font-family: "Open Sans", Arial, sans-serif;
    font-weight: 700;
    font-size: 60px;
    line-height: 1;
    letter-spacing: 1px;
  }
  .tag__sub {
    margin: 6px 0 0;
    font-family: "Open Sans", Arial, sans-serif;
    font-weight: 700;
    font-size: 19px;
    letter-spacing: 0.5px;
  }
  .tag__elevation {
    position: absolute;
    left: 14px; top: 187px; width: 220px; height: 40px;
    background: linear-gradient(180deg, #2a2a2a, #3a3a3a);
  }
  .tag__architect {
    position: absolute;
    left: 0; right: 0; top: 300px;
    margin: 0;
    font-family: "Open Sans", Arial, sans-serif;
    font-size: 10px;
    letter-spacing: 3.5px;
  }

  .headline {
    position: absolute;
    left: 357px; top: 405px;
    margin: 0;
    line-height: 1;
  }
  .headline__main {
    display: block;
    font-weight: 700;
    font-size: 58px;
    letter-spacing: -0.5px;
  }
  .headline__place {
    display: block;
    margin-top: 6px;
    font-weight: 300;
    font-size: 50px;
  }

  .details {
    position: absolute;
    left: 0; top: 534px; width: 848px; height: 213px;
    background: var(--band-grey);
  }
  .details__title {
    position: absolute;
    left: 99px; top: 42px;
    margin: 0;
    font-weight: 700;
    font-size: 19px;
    letter-spacing: 0.3px;
  }
  .details__body {
    position: absolute;
    left: 99px; top: 66px; width: 664px;
    margin: 0;
    font-family: Arial, Helvetica, sans-serif;
    font-size: 17px;
    line-height: 24.5px;
    color: var(--text-grey);
  }

  .price-badge {
    position: absolute;
    left: 96px; top: 903px;
  }

  .contact {
    position: absolute;
    left: 394px; top: 1118px;
    margin: 0;
    font-size: 42px;
    line-height: 1;
  }
  .contact__label { font-weight: 300; }
  .contact__number { font-weight: 700; }
</style>
</head>
<body>
<main class="card">
  <div class="photo photo--bedroom" role="img" aria-label="Bedroom with timber bedside table and lamp"></div>
  <div class="photo photo--kitchen" role="img" aria-label="Kitchen cooktop with kettle and tiled splashback"></div>
  <div class="photo photo--living" role="img" aria-label="Living area with timber frame and indoor plant"></div>

  <div class="tag">
    <svg class="tag__hole" width="32" height="32" viewBox="0 0 32 32" aria-hidden="true">
      <circle cx="16" cy="16" r="16" fill="#ffffff"/>
    </svg>
    <p class="tag__name">K7</p>
    <p class="tag__sub">RESIDENCES</p>
    <div class="tag__elevation" role="img" aria-label="Line elevation of the building facade"></div>
    <p class="tag__architect">BY MARLOW FINCH</p>
  </div>

  <h1 class="headline">
    <span class="headline__main">BEAUTIFUL HOUSE</span>
    <span class="headline__place">IN SURREY</span>
  </h1>

  <section class="details">
    <h2 class="details__title">DESCRIPTION</h2>
    <p class="details__body">1 bed 1 bath with balcony 1 car • Fully furnished • First floor available, First • 1 bed 1 bath with balcony 2 car • Fully furnished • 6th floor unit with stunning views to the city • 1 bed 1 bath with balcony 2 car • Fully furnished, 6th floor unit with stunning • 1 bed 1 bath with balcony 2 car&nbsp; Fully furnished, 6th floor unit with stunning views to the city</p>
  </section>

  <div class="photo photo--exterior" role="img" aria-label="Building exterior walkway with ornamental grasses and street"></div>

  <svg class="price-badge" width="242" height="242" viewBox="0 0 242 242" role="img" aria-label="$240,000 on sale now">
    <defs>
      <radialGradient id="ring" cx="50%" cy="45%" r="55%">
        <stop offset="0.85" stop-color="#ffffff"/>
        <stop offset="1" stop-color="#d4d4d4"/>
      </radialGradient>
    </defs>
    <circle cx="121" cy="121" r="120" fill="url(#ring)"/>
    <circle cx="121" cy="121" r="108" fill="var(--price-red)"/>
    <g transform="rotate(-20 121 121)" fill="#ffffff" font-family="Roboto Condensed, Arial Narrow, sans-serif" text-anchor="middle">
      <text x="121" y="128" font-size="46" font-weight="700">$ 240,000</text>
      <text x="121" y="158" font-size="26" font-weight="400">ON SALES NOW</text>
    </g>
  </svg>

  <p class="contact">
    <span class="contact__label">call now</span>
    <span class="contact__number">07 3000 0199</span>
  </p>
</main>
</body>
</html>
```